Vantrel Web Services

This is a new It services company operating in Perth western Australia

we need a website that is easy to navigate without a cluttered feel to it it should have the following links and pages

About Us
Services
Clients
Contact Us
MY Vantrel (login for clients)

Hi it is a web based IT services company so we would expect customers to come to the website for 2 different purposes the first is to enquire about our services and then as they become customers come to our website to manage their services so whilst they are seperate we want do not want it to look like 2 different websites

hope this helps

Hi to update this we need a home page and templates for sub pages

this is a design brief only and not the coding of the pages or building of the site

```html
<!DOCTYPE html>
<html lang="en">
<head>
<meta charset="utf-8">
<title>Vantrel Web Services</title>
<link href="https://fonts.googleapis.com/css2?family=Noto+Serif:ital,wght@0,400;0,700;1,400;1,700&family=Open+Sans:wght@400;600&family=Roboto+Condensed:wght@400&display=swap" rel="stylesheet">
<style>
:root{
  --blue:#0a2e94;
  --red:#970000;
  --text:#333;
  --muted:#666;
  --line:#d9d9d9;
  --nav-bg:#ececec;
  --white:#fff;
  --social:#cfcfcf;
}
*{box-sizing:border-box;margin:0;padding:0}
html,body{width:810px;height:1200px;overflow:hidden;background:var(--white)}
body{position:relative;font-family:"Noto Serif",Georgia,serif;color:var(--text)}
.abs{position:absolute}

/* header */
.brand{left:48px;top:16px;display:flex;align-items:center;gap:10px}
.brand-dot{width:50px;height:50px;border-radius:50%;background:var(--red)}
.brand-name{font-size:27px;font-weight:700;color:var(--blue);letter-spacing:2px}
.contact{left:416px;top:26px;display:flex;gap:10px;align-items:center}
.contact-lines{font-size:11.5px;font-style:italic;font-weight:700;color:#666;line-height:15px}
.social{left:607px;top:29px;display:flex;gap:6px}
.social span{width:21px;height:21px;border-radius:50%;background:var(--social)}
.social span:first-child{background:var(--blue)}

/* nav */
.nav{left:0;top:81px;width:810px;height:33px;background:var(--nav-bg);border-bottom:2px solid #ddd}
.nav ul{list-style:none;display:flex;position:absolute;left:47px;top:0;height:33px}
.nav li{padding:0 17px;font-size:12.5px;line-height:33px;color:#333;border-right:2px solid #fff}
.nav li.active{background:var(--blue);color:#fff;padding:0 16px}
.search{right:47px;top:81px;width:41px;height:33px;background:var(--red);display:flex;align-items:center;justify-content:center}

/* hero */
.hero{left:0;top:114px;width:810px;height:333px;background:linear-gradient(100deg,#f4f4f4 0%,#e6e6e6 45%,#d8d8d8 100%);border-bottom:3px solid #c8c8c8}
.hero-art{left:395px;top:115px;width:340px;height:332px;background:radial-gradient(ellipse at 50% 40%,#f2f2f2 0%,#d0d0d0 55%,#bdbdbd 100%)}
.hero-title{left:48px;top:168px;font-style:italic;font-weight:700;font-size:37px;line-height:50px}
.hero-title .l1{color:var(--blue)}
.hero-title .l2{color:var(--red)}
.hero-copy{left:47px;top:284px;width:345px;font-size:10.6px;line-height:17.2px;color:#222}
.dots{left:333px;top:436px;display:flex;gap:7px}
.dots span{width:22px;height:22px;border-radius:50%;background:#555}
.dots span:first-child{background:var(--red)}

/* welcome */
.welcome-title{left:0;width:810px;top:478px;text-align:center;font-style:italic;font-weight:700;font-size:23px;color:#666}
.welcome-title .b{color:var(--blue)}.welcome-title .r{color:var(--red)}
.welcome-copy{left:58px;top:522px;width:696px;text-align:center;font-size:9.3px;line-height:17.3px;color:#555}

/* services band */
.band{left:0;top:631px;width:810px;height:148px;background:var(--red);border-top:2px solid var(--blue)}
.svc-icon{top:594px;width:64px;height:64px;border-radius:50%;background:var(--red);display:flex;align-items:center;justify-content:center}
.svc-icon.first{border-top:3px solid var(--blue)}
.svc{top:668px;width:240px;text-align:center;color:#fff}
.svc h3{font-style:italic;font-weight:700;font-size:15px;margin-bottom:8px}
.svc p{font-size:10.4px;line-height:17.3px}
.more{top:759px;width:74px;height:20px;background:#fff;font-style:italic;font-weight:700;font-size:9.5px;text-align:center;line-height:21px;color:#777}
.more.first{color:var(--blue)}

/* why */
.why-title{left:48px;top:806px;font-style:italic;font-weight:700;font-size:23px}
.why-title .b{color:var(--blue)}.why-title .r{color:var(--red)}
.why-rule{left:47px;top:840px;width:177px;height:1px;background:var(--line)}
.why-sub{left:47px;top:850px;font-style:italic;font-weight:700;font-size:11.2px;color:var(--blue)}
.why-copy{left:47px;top:873px;width:490px;font-size:9.3px;line-height:14.5px;color:#444}
.why-lead{left:47px;top:921px;font-size:11.2px;color:var(--blue)}
.ticks{left:50px;top:944px;list-style:none;font-size:9.3px;color:#444}
.ticks li{display:flex;align-items:center;gap:6px;height:21.5px}

/* quote */
.quote{left:559px;top:814px;width:204px;height:196px;border:1px solid var(--blue);background:#fff;box-shadow:0 2px 4px rgba(0,0,0,.15)}
.quote h4{background:var(--blue);color:#fff;font-family:"Roboto Condensed",Arial,sans-serif;font-weight:400;font-size:14px;height:24px;line-height:24px;padding-left:8px}
.quote p{font-family:"Open Sans",Arial,sans-serif;font-size:9px;line-height:14px;color:#666;padding:8px 7px 0}
.field{margin:7px 7px 0;height:22px;border:1px solid #ccc;background:#f7f7f7;font-family:"Open Sans",Arial,sans-serif;font-size:9px;line-height:20px;color:#777;padding-left:6px}
.field:first-of-type{margin-top:9px}
.signup{right:0;bottom:0;width:62px;height:20px;background:var(--blue);clip-path:polygon(9px 0,100% 0,100% 100%,0 100%);color:#fff;font-style:italic;font-weight:700;font-size:10.5px;line-height:20px;text-align:right;padding-right:10px}

/* tweet */
.tweet-bg{left:0;top:1030px;width:810px;height:130px;background:linear-gradient(180deg,#cfcfcf 0%,#efefef 35%,#e8e8e8 70%,#bdbdbd 100%)}
.tweet{left:47px;top:1060px;width:716px;height:71px;background:#fff;border-left:3px solid var(--blue);border-right:3px solid var(--blue)}
.tweet-mark{left:14px;top:23px;width:24px;height:24px;border-radius:50%;background:var(--blue)}
.tweet-text{left:53px;top:19px;width:500px;font-size:10.8px;line-height:16px;color:#555}
.tweet-text a{color:var(--blue);text-decoration:none}
.tweet-time{right:8px;top:26px;font-style:italic;font-weight:700;font-size:12px;color:var(--blue)}

/* footer */
.foot-links{left:47px;top:1175px;font-size:9.3px;color:var(--blue)}
.foot-links .home{color:var(--red)}
.foot-links i{font-style:normal;color:#888;margin:0 4px}
.foot-legal{right:50px;top:1176px;font-size:9.3px;color:#777}
.foot-legal b{font-weight:400;color:var(--blue)}
</style>
</head>
<body>

<header>
  <div class="abs brand"><span class="brand-dot"></span><span class="brand-name">VANTREL</span></div>
  <div class="abs contact">
    <svg width="32" height="26" viewBox="0 0 32 26" aria-hidden="true">
      <rect x="1" y="8" width="22" height="15" fill="#0a2e94"/>
      <path d="M1 8 L12 17 L23 8" fill="none" stroke="#fff" stroke-width="1.5"/>
      <rect x="19" y="1" width="12" height="12" rx="2" fill="#222"/>
      <path d="M22 4 q0 5 6 6 l1-2 -2-1 -1 1 q-2-1-2-3 l1-1 -1-2z" fill="#fff"/>
    </svg>
    <div class="contact-lines">Call: +123 555 0142<br>info@vantrel.com</div>
  </div>
  <div class="abs social" aria-label="Social links"><span></span><span></span><span></span><span></span><span></span><span></span></div>
</header>

<nav class="abs nav">
  <ul>
    <li class="active">Home</li><li>About Us</li><li>Services</li><li>Clients</li><li>Contact Us</li><li>MY Vantrel</li>
  </ul>
</nav>
<div class="abs search">
  <svg width="20" height="20" viewBox="0 0 20 20" aria-hidden="true"><circle cx="8" cy="8" r="6" fill="none" stroke="#fff" stroke-width="2.5"/><path d="M12.5 12.5 L18 18" stroke="#fff" stroke-width="3" stroke-linecap="round"/></svg>
</div>

<section>
  <div class="abs hero" role="img" aria-label="Soft grey cloudy sky backdrop"></div>
  <div class="abs hero-art" role="img" aria-label="Light bulbs on coloured cables in a pot of pebbles"></div>
  <h1 class="abs hero-title"><span class="l1">We bring your</span><br><span class="l2">IDEAS to REALITY</span></h1>
  <p class="abs hero-copy">In May of 1899 Edmund Hale wrote a letter to the Halden Institution with an idea in mind. On December 17, 1903 Edmund, and his brother Arthur, invented and built the world’s first airplane — and conducted the world’s first successfully controlled, powered and heavier-than-air flight.</p>
  <div class="abs dots"><span></span><span></span><span></span><span></span></div>
</section>

<section>
  <h2 class="abs welcome-title">Welcome to <span class="b">VANTREL</span></h2>
  <p class="abs welcome-copy">Lorem ipsum dolor sit amet, consectetur adipiscing elit. In ut ligula vitae dolor faucibus commodo accumsan nec lectus. Fusce ac magna vel urna semper dapibus. Sed non malesuada massa, eget tincidunt lectus. Ut eget ullamcorper turpis. Aliquam sit amet diam egestas, interdum orci at, sodales risus. Integer suscipit in magna eu sagittis. Morbi nec neque orci.</p>
</section>

<section>
  <div class="abs band"></div>
  <div class="abs svc-icon first" style="left:120px">
    <svg width="34" height="24" viewBox="0 0 34 24" aria-hidden="true"><path d="M9 4 L2 12 L9 20 M25 4 L32 12 L25 20 M20 2 L14 22" fill="none" stroke="#fff" stroke-width="3"/></svg>
  </div>
  <div class="abs svc-icon" style="left:371px">
    <svg width="30" height="30" viewBox="0 0 30 30" aria-hidden="true"><rect x="2" y="5" width="26" height="17" fill="none" stroke="#fff" stroke-width="2.5"/><rect x="11" y="22" width="8" height="4" fill="#fff"/><rect x="7" y="26" width="16" height="2" fill="#fff"/><rect x="12" y="2" width="7" height="13" rx="1" fill="#fff"/></svg>
  </div>
  <div class="abs svc-icon" style="left:622px">
    <svg width="34" height="34" viewBox="0 0 34 34" aria-hidden="true"><circle cx="17" cy="15" r="8" fill="#fff"/><rect x="13" y="23" width="8" height="6" fill="#fff"/><path d="M17 1v3M5 5l2 2M29 5l-2 2M1 15h3M30 15h3" stroke="#fff" stroke-width="2"/></svg>
  </div>

  <div class="abs svc" style="left:34px"><h3>Software Development</h3><p>After many years in Software Project Delivery, Corvane Network can help you at every stage of your project.</p></div>
  <div class="abs svc" style="left:285px"><h3>Application Management</h3><p>90% of the cost involved in managing software systems lies in maintenance phase – which is often neglected</p></div>
  <div class="abs svc" style="left:536px"><h3>Improvement Management</h3><p>We live today in a very high-paced society – organization who wish to excels will need to constantly evolve and innovate.</p></div>

  <div class="abs more first" style="left:117px">Read more</div>
  <div class="abs more" style="left:368px">Read more</div>
  <div class="abs more" style="left:619px">Read more</div>
</section>

<section>
  <h2 class="abs why-title"><span class="b">Why</span> <span class="r">VANTREL</span></h2>
  <div class="abs why-rule"></div>
  <p class="abs why-sub">Trustworthy IT Tech support for companies in and around Perth, Australia</p>
  <p class="abs why-copy">Lorem ipsum dolor sit amet, consectetur adipiscing elit. Donec ut nisl sed eros venenatis fermentum at sit amet felis. Curabitur et magna dui. Integer ipsum neque, lobortis nec luctus eget, facilisis non nisi. Vivamus ultricies erat vel lorem sodales suscipitNam eleifend diam sit amet mi mattis graida.</p>
  <p class="abs why-lead">Phasellus ornare dolor justo, vitae auctor lacus elementum faucibus:</p>
  <ul class="abs ticks">
    <li><svg width="8" height="8" viewBox="0 0 8 8" aria-hidden="true"><path d="M1 4 L3 6.5 L7 1" fill="none" stroke="#0a2e94" stroke-width="1.6"/></svg>Ut non adipiscing enim, vitae blandit ipsum. Aenean et mi turpis.</li>
    <li><svg width="8" height="8" viewBox="0 0 8 8" aria-hidden="true"><path d="M1 4 L3 6.5 L7 1" fill="none" stroke="#0a2e94" stroke-width="1.6"/></svg>Maecenas gravida sed purus ut faucibus. Donec quis mi nunc.</li>
    <li><svg width="8" height="8" viewBox="0 0 8 8" aria-hidden="true"><path d="M1 4 L3 6.5 L7 1" fill="none" stroke="#0a2e94" stroke-width="1.6"/></svg>Praesent venenatis eu dui ut gravida. Cras vitae elit quis enim</li>
  </ul>

  <form class="abs quote">
    <h4>Request Quote</h4>
    <p>Fill out the form and our staff will be in touch with you shortly.</p>
    <div class="field">Name:</div>
    <div class="field">Phone :</div>
    <div class="field">Email Adreess:</div>
    <div class="abs signup">Sign up</div>
  </form>
</section>

<section>
  <div class="abs tweet-bg" role="img" aria-label="Blurred grey office backdrop"></div>
  <div class="abs tweet">
    <span class="abs tweet-mark"></span>
    <p class="abs tweet-text">Lorem ipsum dolor sit amet, consectetur adipiscing elit. <a>Aenean hendrerit</a>, tellus in fermentum pellentesque . onsectetur adipiscing elit</p>
    <span class="abs tweet-time">2 hour ago</span>
  </div>
</section>

<footer>
  <div class="abs foot-links"><span class="home">Home</span><i>/</i>About<i>/</i>Services<i>/</i>Clients<i>/</i>Contacts<i>/</i>MY Vantrel</div>
  <div class="abs foot-legal">© 2014 <b>Vantrel.</b>&nbsp; Privacy Policy &nbsp;/&nbsp; Term of Use &nbsp;/&nbsp; Site Map</div>
</footer>

</body>
</html>
```